bRevik Equity Advisors Website

We are interested in developing a complete website and long term maintenance with the developer we choose through this contest.

Brevik is a financial consulting company. We will have a website that capitalizes on the initial costs of retaining a client by providing additional services the client needs and tyically spend using 3rd parties.

The primary function of the website will be structured as a sales tool to retain and provide financial services to the client. Also, to provide other services that are integral to starting, building, and growing a business in order to increase creditibility and maintain client loyalty.

Through a combination of in-house "white label" services as well well chosen outside professional services as "affiliates".

The website home page must be a an instant curb-side appeal and representation of our desired extraordinary image. That image is a robust, innovative (bRevik), with a sophistication that creates an instant emotion of excitement and confidence that they have finally found that "needle in the haystack" they have been seeking. The feeling that they are compelled to take action lest they lose our contact information and are doomed to sink to the mediocrity that most business accept through a lack of effort and forsite.

Reason: Emails were going to the wrong account and I didn't receive any notices of questions or designs being posted.

Target Market(s)

Startup, growth and advancing companies seeking capital and other business services such as website and corporate image design, legal, marketing, asset management, investment and business consulting, etc.

Industry/Entity Type

Financial

Requirements
Must have
• We want to see your creativity
Nice to have
Should not have

```html
<!DOCTYPE html>
<html lang="en">
<head>
<meta charset="utf-8">
<title>bRevik Equity Advisors</title>
<link href="https://fonts.googleapis.com/css2?family=Source+Sans+3:wght@300;400;600&display=swap" rel="stylesheet">
<style>
:root{
  --bg-deep:#021a06;
  --bg-glow:#0f6a22;
  --shell:#bdbec0;
  --shell-dark:#111;
  --panel:#000;
  --lime:#8dc63f;
  --text-light:#f2f2f2;
  --text-muted:#8e8e8e;
  --grey-mid:#6d6e70;
  --scroll:#0d5a1e;
}
*{box-sizing:border-box;margin:0;padding:0}
html,body{width:1200px;height:905px;overflow:hidden}
body{
  font-family:"Source Sans 3",sans-serif;
  background:radial-gradient(ellipse at 50% 50%,var(--bg-glow) 0%,#06380f 55%,var(--bg-deep) 100%);
  position:relative;
}
.site{
  position:absolute;left:149px;top:26px;width:904px;height:854px;
  border-radius:22px;
  background:linear-gradient(180deg,var(--shell) 0%,var(--shell) 52%,#5a5b5d 80%,var(--shell-dark) 94%,#000 100%);
  box-shadow:0 6px 18px rgba(0,0,0,.6);
}
.abs{position:absolute}
.languages{left:36px;top:18px;font-size:15px;color:var(--grey-mid);word-spacing:4px}
.search-label{left:556px;top:14px;font-size:17px;letter-spacing:7px;color:var(--grey-mid)}
.search-box{left:665px;top:12px;width:212px;height:25px;border-radius:5px;background:#555659;border:2px solid #3e3f41;box-shadow:inset 0 2px 4px rgba(0,0,0,.6)}
.header{
  left:24px;top:47px;width:859px;height:200px;border-radius:18px 18px 0 0;
  background:linear-gradient(180deg,#3b3c3e 0%,#6f7072 45%,#a7a8aa 100%);
  overflow:hidden;
}
.brand{left:48px;top:40px;font-size:86px;font-weight:600;color:#2c2d2f;letter-spacing:-1px;line-height:1}
.tagline{left:119px;top:124px;font-size:14px;letter-spacing:7px;color:#d8d8d8}
.header-photo{
  left:450px;top:17px;width:397px;height:155px;
  clip-path:ellipse(72% 90% at 72% 35%);
  background:linear-gradient(135deg,#e9e5e1 0%,#c9b6a3 40%,#8a7565 70%,#d8d3cf 100%);
}
.nav{left:0;top:0}
.tab{
  position:absolute;display:flex;justify-content:center;align-items:flex-start;
  background:var(--panel);color:var(--lime);font-size:16px;border-radius:6px 6px 0 0;
}
.tab.home{left:42px;top:195px;width:90px;height:49px;padding-top:11px}
.tab.about{left:140px;top:208px;width:91px;height:64px;padding-top:9px;background:linear-gradient(180deg,#000 60%,#0b0b0d 100%)}
.tab.services{left:238px;top:208px;width:91px;height:64px;padding-top:9px;background:linear-gradient(180deg,#000 60%,#0b0b0d 100%)}
.tab.contact{left:335px;top:208px;width:92px;height:64px;padding-top:9px;background:linear-gradient(180deg,#000 60%,#0b0b0d 100%)}
.main{left:25px;top:243px;width:856px;height:557px;background:var(--panel);border-radius:8px;overflow:hidden}
.welcome{left:23px;top:38px;font-size:22px;font-weight:400;color:var(--lime);line-height:1}
.welcome small{font-size:16px}
.intro{left:24px;top:69px;width:345px;font-size:13px;font-weight:400;line-height:16.2px;color:var(--text-light)}
.intro p{margin-bottom:9px}
.video-well{left:385px;top:41px;width:418px;height:105px;background:linear-gradient(180deg,#000 0%,#555 60%,#7a7b7d 100%);border-radius:6px 6px 0 0}
.video{left:421px;top:73px;width:346px;height:147px;background:#000;padding:7px 7px 0 7px}
.video-screen{width:100%;height:100%;background:linear-gradient(180deg,#3c3d3f,#464749);position:relative}
.video-name{left:0;right:0;top:32px;text-align:center;font-size:42px;font-weight:600;color:#5c5d5f;line-height:1}
.video-tag{left:0;right:0;top:82px;text-align:center;font-size:6px;letter-spacing:3px;color:#777}
.play{left:148px;top:104px}
.scrollbar{left:829px;top:36px;width:16px;height:505px;border-radius:4px;background:linear-gradient(90deg,#062e0d,var(--scroll),#06300e)}
.scroll-thumb{left:833px;top:60px;width:8px;height:34px;border-radius:3px;background:linear-gradient(90deg,#2e8a3c,#4fb34f)}
.news{left:23px;top:301px;width:791px;height:240px;border-radius:8px;background:linear-gradient(180deg,#8d8e90 0%,#5f6062 12%,#000 32%,#000 100%)}
.news-inner{position:absolute;left:6px;top:6px;right:6px;bottom:0;background:linear-gradient(180deg,#2f3032 0%,#000 45%);border-radius:5px 5px 0 0}
.news-text{left:25px;top:30px;width:300px;font-size:12.2px;font-weight:400;line-height:15.6px;color:var(--text-muted)}
.news-text p{margin-bottom:15px}
.read-more{left:234px;top:209px;font-size:15px;color:var(--lime);line-height:1.2}
.news-prev{left:379px;top:12px;font-size:10px;color:var(--lime);display:flex;align-items:center;gap:3px}
.news-next{left:648px;top:12px;font-size:10px;color:var(--lime);display:flex;align-items:center;gap:5px}
.news-photo-frame{left:338px;top:30px;width:400px;height:198px;border-radius:7px;background:#8a8b8d;padding:5px}
.news-photo{width:100%;height:100%;border-radius:4px;background:linear-gradient(160deg,#d8c7b2 0%,#3b6fcf 22%,#1a4fb5 55%,#4aa0ef 100%)}
.footer{left:0;top:819px;width:904px;font-size:15px;color:var(--text-muted);line-height:1.2}
.copyright{left:33px;top:0}
.footer-note{left:317px;top:0}
.footer-links{left:607px;top:0;color:var(--grey-mid)}
.footer-links a{color:var(--lime);text-decoration:none}
</style>
</head>
<body>
<div class="site">
  <div class="abs languages">English Hindi Spanish</div>
  <div class="abs search-label">Seacrh:</div>
  <div class="abs search-box"></div>

  <header class="abs header">
    <div class="abs brand">bRevik</div>
    <div class="abs tagline">EQUITY ADVISORS</div>
    <div class="abs header-photo" role="img" aria-label="Photo of three smiling business colleagues looking at a screen"></div>
  </header>

  <main class="abs main">
    <h1 class="abs welcome">WELCOME <small>TO OUR COMPANY</small></h1>
    <div class="abs intro">
      <p>Lorem ipsum dolor sit amet, consectetur adipisicing elit, sed do eiusmod tempor incididunt ut labore et dolore magna al Voluptate velit esse cillum dolore eu fugiat nulla pariatur. Excepteur sint... occaecat cupidatat non pro.</p>
      <p>Lorem ipsum dolor sit amet, consectetur adipisicing elit, sed do eiusmod tempor incididunt ut labore et dolore magna al Voluptate velit..</p>
      <p>Lorem ipsum dolor sit amet, consectetur adipisicing elit, sed do eiusmod tempor incididunt ut labore et dolore magna al Voluptate velit esse cillum dolore eu fugiat nulla pariatur. Excepteur sint... occaecat cupidatat non pro.</p>
    </div>

    <div class="abs video-well"></div>
    <div class="abs video">
      <div class="video-screen">
        <div class="abs video-name">bRevik</div>
        <div class="abs video-tag">EQUITY ADVISORS</div>
        <svg class="abs play" width="30" height="24" viewBox="0 0 30 24"><defs><linearGradient id="playFill" x1="0" y1="0" x2="0" y2="1"><stop offset="0" stop-color="#c8ef8a"/><stop offset="1" stop-color="#5ea82a"/></linearGradient></defs><path d="M2 2 L28 12 L2 22 Z" fill="url(#playFill)"/></svg>
      </div>
    </div>

    <div class="abs scrollbar"></div>
    <div class="abs scroll-thumb"></div>

    <section class="abs news">
      <div class="news-inner"></div>
      <div class="abs news-prev"><svg width="14" height="10" viewBox="0 0 14 10"><path d="M0 5 L14 0 L14 10 Z" fill="#d0d0d0"/></svg>Last New</div>
      <div class="abs news-next">Next New<svg width="14" height="10" viewBox="0 0 14 10"><path d="M14 5 L0 0 L0 10 Z" fill="#d0d0d0"/></svg></div>
      <div class="abs news-text">
        <p>Lorem ipsum dolor sit amet, consectetur adipisicing elit, sed do eiusmod tempor incididunt ut labore et dolore magna aliqua. Ut enim ad minim veniam, quis nostrud exercitation ullamco laboris nisi ut aliquip ex ea commodo consequat.</p>
        <p>Duis aute irure dolor in reprehenderit in voluptate velit esse cillum dolore eu fugiat nulla pariatur. Excepteur sint occaecat cupidatat non proident, sunt in culpa qui officia deserunt mollit anim id est laborum."</p>
      </div>
      <div class="abs read-more">Read&nbsp; More...</div>
      <div class="abs news-photo-frame">
        <div class="news-photo" role="img" aria-label="Photo of a pen pointing at a blue stock market chart"></div>
      </div>
    </section>
  </main>

  <nav class="abs nav">
    <div class="tab home">Home</div>
    <div class="tab about">About Us</div>
    <div class="tab services">Services</div>
    <div class="tab contact">Contact Us</div>
  </nav>

  <footer class="abs footer">
    <div class="abs copyright">©2011-2020 bRevik. All rights reserved.</div>
    <div class="abs footer-note">Lorem ipsum dolor sit amet, consectetur</div>
    <div class="abs footer-links"><a href="#">Home</a> | <a href="#">About Us</a> | <a href="#">Services</a> | <a href="#">Contact Us</a></div>
  </footer>
</div>
</body>
</html>
```